Design für 3-Monatskalender
Zielgruppe
Hallo, wir benötigen ein Design bzw. fertige Druckdaten für einen 3 Monatskalender mit den Feiertagen aus DE, AT und CH.
Format ist DIN A6, der Kalender wird benötigt für das Jahr 2024 und 2025.
Aufgabenstellung
Format: DIN A6
Kalendarium 2024 und 2025
Feiertage aus DE, AT und CH
Beispiel anbei, wichtig ist, das wir einen Magnetischen Ring als Datumsschieber nehmen. Der Ring hat die Maße: Durchmesser = 12mm Innendruchmesser = 10mm

```html
<!DOCTYPE html>
<html lang="de">
<head>
<meta charset="utf-8">
<title>3-Monatskalender 2024</title>
<link rel="stylesheet" href="https://fonts.googleapis.com/css2?family=Rubik:wght@300;400;600;700&display=swap">
<style>
  :root {
    --paper: #ffffff;
    --ink: #1a1a1a;
    --muted: #8c8c8c;
    --frame: #9a9a9a;
    --ring: #a3a3a3;
  }
  html, body { margin: 0; padding: 0; width: 1200px; height: 1200px; overflow: hidden; background: var(--paper); }
  .calendar { display: block; width: 1200px; height: 1200px; font-family: 'Rubik', sans-serif; }
  .sheet { fill: var(--paper); stroke: var(--frame); stroke-width: 2.5; }
  .sheet-top { stroke: #333; stroke-width: 2; }
  .month-title { font-size: 31px; font-weight: 400; letter-spacing: 2px; fill: var(--ink); text-anchor: middle; }
  .weekday, .kw-label { font-size: 20px; font-weight: 300; fill: var(--muted); text-anchor: middle; }
  .week-no { font-size: 21px; font-weight: 300; fill: var(--ink); text-anchor: middle; }
  .day { font-size: 42px; font-weight: 700; fill: var(--ink); text-anchor: middle; }
  .row-rule { stroke: #555; stroke-width: 1.2; stroke-dasharray: 1.5 2.2; }
  .holidays { font-size: 15px; font-weight: 300; fill: var(--ink); }
  .holidays .label { font-weight: 600; }
  .date-ring { fill: none; stroke: var(--ring); stroke-width: 6; }
</style>
</head>
<body>
<svg class="calendar" viewBox="0 0 1400 1400" xmlns="http://www.w3.org/2000/svg">
  <rect class="sheet" x="287" y="119" width="824" height="1162"/>
  <line class="sheet-top" x1="286" y1="119" x2="1112" y2="119"/>

  <!-- Januar -->
  <g class="month month-jan">
    <text class="month-title" x="721" y="182">JANUAR 2024</text>
    <g>
      <text class="kw-label" x="349" y="220">KW</text>
      <text class="weekday" x="422" y="220">MO</text><text class="weekday" x="522" y="220">DI</text><text class="weekday" x="622" y="220">MI</text><text class="weekday" x="721" y="220">DO</text><text class="weekday" x="821" y="220">FR</text><text class="weekday" x="921" y="220">SA</text><text class="weekday" x="1020" y="220">SO</text>
    </g>
    <line class="row-rule" x1="325" y1="283" x2="1071" y2="283"/>
    <line class="row-rule" x1="325" y1="338" x2="1071" y2="338"/>
    <line class="row-rule" x1="325" y1="393" x2="1071" y2="393"/>
    <line class="row-rule" x1="325" y1="448" x2="1071" y2="448"/>
    <g>
      <text class="week-no" x="349" y="264">1</text><text class="day" x="422" y="272">1</text><text class="day" x="522" y="272">2</text><text class="day" x="622" y="272">3</text><text class="day" x="721" y="272">4</text><text class="day" x="821" y="272">5</text><text class="day" x="921" y="272">6</text><text class="day" x="1020" y="272">7</text>
      <text class="week-no" x="349" y="319">2</text><text class="day" x="422" y="327">8</text><text class="day" x="522" y="327">9</text><text class="day" x="622" y="327">10</text><text class="day" x="721" y="327">11</text><text class="day" x="821" y="327">12</text><text class="day" x="921" y="327">13</text><text class="day" x="1020" y="327">14</text>
      <text class="week-no" x="349" y="374">3</text><text class="day" x="422" y="382">15</text><text class="day" x="522" y="382">16</text><text class="day" x="622" y="382">17</text><text class="day" x="721" y="382">18</text><text class="day" x="821" y="382">19</text><text class="day" x="921" y="382">20</text><text class="day" x="1020" y="382">21</text>
      <text class="week-no" x="349" y="429">4</text><text class="day" x="422" y="437">22</text><text class="day" x="522" y="437">23</text><text class="day" x="622" y="437">24</text><text class="day" x="721" y="437">25</text><text class="day" x="821" y="437">26</text><text class="day" x="921" y="437">27</text><text class="day" x="1020" y="437">28</text>
      <text class="week-no" x="349" y="484">5</text><text class="day" x="422" y="492">29</text><text class="day" x="522" y="492">30</text><text class="day" x="622" y="492">31</text>
    </g>
    <text class="holidays" x="681" y="469"><tspan class="label">Feiertage:</tspan> 1. 1. Neujahr (D, A, CH), 2. 1. Berchtoldstag</text>
    <text class="holidays" x="681" y="489">(CH), 6. 1. Heilige Drei Könige (CH),</text>
  </g>

  <!-- Februar -->
  <g class="month month-feb">
    <text class="month-title" x="721" y="552">FEBRUAR 2024</text>
    <g>
      <text class="kw-label" x="349" y="590">KW</text>
      <text class="weekday" x="422" y="590">MO</text><text class="weekday" x="522" y="590">DI</text><text class="weekday" x="622" y="590">MI</text><text class="weekday" x="721" y="590">DO</text><text class="weekday" x="821" y="590">FR</text><text class="weekday" x="921" y="590">SA</text><text class="weekday" x="1020" y="590">SO</text>
    </g>
    <line class="row-rule" x1="325" y1="653" x2="1071" y2="653"/>
    <line class="row-rule" x1="325" y1="708" x2="1071" y2="708"/>
    <line class="row-rule" x1="325" y1="763" x2="1071" y2="763"/>
    <line class="row-rule" x1="325" y1="818" x2="1071" y2="818"/>
    <g>
      <text class="week-no" x="349" y="634">5</text><text class="day" x="721" y="642">1</text><text class="day" x="821" y="642">2</text><text class="day" x="921" y="642">3</text><text class="day" x="1020" y="642">4</text>
      <text class="week-no" x="349" y="689">6</text><text class="day" x="422" y="697">5</text><text class="day" x="522" y="697">6</text><text class="day" x="622" y="697">7</text><text class="day" x="721" y="697">8</text><text class="day" x="821" y="697">9</text><text class="day" x="921" y="697">10</text><text class="day" x="1020" y="697">11</text>
      <text class="week-no" x="349" y="744">7</text><text class="day" x="422" y="752">12</text><text class="day" x="522" y="752">13</text><text class="day" x="622" y="752">14</text><text class="day" x="721" y="752">15</text><text class="day" x="821" y="752">16</text><text class="day" x="921" y="752">17</text><text class="day" x="1020" y="752">18</text>
      <text class="week-no" x="349" y="799">8</text><text class="day" x="422" y="807">19</text><text class="day" x="522" y="807">20</text><text class="day" x="622" y="807">21</text><text class="day" x="721" y="807">22</text><text class="day" x="821" y="807">23</text><text class="day" x="921" y="807">24</text><text class="day" x="1020" y="807">25</text>
      <text class="week-no" x="349" y="855">9</text><text class="day" x="422" y="863">26</text><text class="day" x="522" y="863">27</text><text class="day" x="622" y="863">28</text><text class="day" x="721" y="863">29</text>
    </g>
    <circle class="date-ring" cx="723" cy="626" r="43"/>
  </g>

  <!-- März -->
  <g class="month month-mar">
    <text class="month-title" x="721" y="922">MÄRZ 2024</text>
    <g>
      <text class="kw-label" x="349" y="960">KW</text>
      <text class="weekday" x="422" y="960">MO</text><text class="weekday" x="522" y="960">DI</text><text class="weekday" x="622" y="960">MI</text><text class="weekday" x="721" y="960">DO</text><text class="weekday" x="821" y="960">FR</text><text class="weekday" x="921" y="960">SA</text><text class="weekday" x="1020" y="960">SO</text>
    </g>
    <line class="row-rule" x1="325" y1="1023" x2="1071" y2="1023"/>
    <line class="row-rule" x1="325" y1="1078" x2="1071" y2="1078"/>
    <line class="row-rule" x1="325" y1="1133" x2="1071" y2="1133"/>
    <line class="row-rule" x1="325" y1="1188" x2="1071" y2="1188"/>
    <g>
      <text class="week-no" x="349" y="1003">9</text><text class="day" x="821" y="1011">1</text><text class="day" x="921" y="1011">2</text><text class="day" x="1020" y="1011">3</text>
      <text class="week-no" x="349" y="1058">10</text><text class="day" x="422" y="1066">4</text><text class="day" x="522" y="1066">5</text><text class="day" x="622" y="1066">6</text><text class="day" x="721" y="1066">7</text><text class="day" x="821" y="1066">8</text><text class="day" x="921" y="1066">9</text><text class="day" x="1020" y="1066">10</text>
      <text class="week-no" x="349" y="1113">11</text><text class="day" x="422" y="1121">11</text><text class="day" x="522" y="1121">12</text><text class="day" x="622" y="1121">13</text><text class="day" x="721" y="1121">14</text><text class="day" x="821" y="1121">15</text><text class="day" x="921" y="1121">16</text><text class="day" x="1020" y="1121">17</text>
      <text class="week-no" x="349" y="1168">12</text><text class="day" x="422" y="1176">18</text><text class="day" x="522" y="1176">19</text><text class="day" x="622" y="1176">20</text><text class="day" x="721" y="1176">21</text><text class="day" x="821" y="1176">22</text><text class="day" x="921" y="1176">23</text><text class="day" x="1020" y="1176">24</text>
      <text class="week-no" x="349" y="1224">13</text><text class="day" x="422" y="1232">25</text><text class="day" x="522" y="1232">26</text><text class="day" x="622" y="1232">27</text><text class="day" x="721" y="1232">28</text><text class="day" x="821" y="1232">29</text><text class="day" x="921" y="1232">30</text><text class="day" x="1020" y="1232">31</text>
    </g>
    <text class="holidays" x="515" y="1007"><tspan class="label">Feiertage:</tspan> 19. 3. Josefstag (A, CH)</text>
  </g>
</svg>
</body>
</html>
```